Belford & Company

We are a boutique commercial real estate firm. For our Business card design - sleek, modern, yet high-end/classy. Please see our website: belfordandcompany.example for details.

We currently need 2 business card names and the ability to add/change the business card information -
Name, Title, Address, Office #, Mobile #, Fax, Email and company website.

Industry/Entity Type

Real Estate

Contact Information for Business Card

Business card design - sleek, modern, yet high-end/classy. Please see our website: belfordandcompany.example for details.

Also, we'd like to have our slogan "Precision Defines Every Deal." somewhere in there. We'd like to make some part of it raised or a different texture if possible.
Color #'s:
blue 19 36 128
light gray 222 222 221
dark gray 107 120 128

Also, we'd like to have our slogan "Precision Defines Every Deal." somewhere in there. We'd like to make some part of it raised or a different texture if possible - grey on one side and blue on the other - rounded edges preferred. Maybe either metal/silver/grey raised logo on the back. Thank you!!

Requirements
Must have
• Sleek, modern, clean and classy design

```html
<!DOCTYPE html>
<html lang="en">
<head>
<meta charset="utf-8">
<title>Belford &amp; Company – Business Card</title>
<link href="https://fonts.googleapis.com/css2?family=Montserrat:wght@400;600;700&display=swap" rel="stylesheet">
<style>
  :root {
    --brand-blue: #1e2a78;
    --brand-blue-soft: #2f3a8a;
    --light-gray: #dededd;
    --dark-gray: #6b7880;
    --paper: #ffffff;
    --backdrop: #ececec;
  }
  * { margin: 0; padding: 0; box-sizing: border-box; }
  html, body { width: 1200px; height: 800px; overflow: hidden; }
  body {
    background: var(--backdrop);
    font-family: 'Montserrat', sans-serif;
    position: relative;
  }
  .card {
    position: absolute;
    top: 278px;
    width: 420px;
    height: 240px;
    border-radius: 6px;
    overflow: hidden;
  }
  .card-back {
    left: 141px;
    background: linear-gradient(160deg, var(--brand-blue-soft) 0%, var(--brand-blue) 60%, #283488 100%);
  }
  .card-back .texture { position: absolute; inset: 0; }
  .card-back .brand-name {
    position: absolute;
    right: 30px;
    bottom: 46px;
    color: var(--paper);
    font-weight: 700;
    font-size: 15px;
    letter-spacing: 0.04em;
    text-transform: uppercase;
    display: flex;
    align-items: center;
    gap: 8px;
    white-space: nowrap;
  }
  .brand-square {
    width: 12px; height: 12px;
    flex-shrink: 0;
    background: var(--light-gray);
  }
  .card-front {
    left: 637px;
    background: var(--paper);
  }
  .card-front .brand-name {
    position: absolute;
    left: 32px;
    top: 108px;
    width: 140px;
    color: var(--brand-blue);
    font-weight: 700;
    font-size: 14px;
    line-height: 1.25;
    letter-spacing: 0.04em;
    text-transform: uppercase;
    display: flex;
    align-items: center;
    gap: 8px;
  }
  .card-front .brand-square { background: var(--brand-blue); }
  .divider {
    position: absolute;
    left: 179px;
    top: 45px;
    width: 1px;
    height: 140px;
    background: var(--dark-gray);
    opacity: 0.6;
  }
  .contact {
    position: absolute;
    left: 196px;
    top: 52px;
    right: 14px;
    color: var(--brand-blue);
  }
  .person-name { font-weight: 700; font-size: 16px; letter-spacing: 0.02em; line-height: 1; }
  .person-title { font-size: 11px; margin-top: 1px; }
  .contact-list { list-style: none; margin-top: 5px; font-size: 10.5px; line-height: 14px; }
  .contact-list li { display: flex; align-items: flex-start; gap: 8px; white-space: nowrap; }
  .contact-list li.gap { margin-top: 5px; }
  .contact-list svg { width: 10px; height: 10px; margin-top: 2px; flex-shrink: 0; fill: var(--brand-blue); }
  .slogan-band {
    position: absolute;
    left: 0; right: 0;
    top: 203px;
    height: 21px;
    background: var(--brand-blue);
    color: var(--paper);
    font-weight: 600;
    font-size: 10px;
    letter-spacing: 0.08em;
    text-transform: uppercase;
    display: flex;
    align-items: center;
    justify-content: center;
  }
</style>
</head>
<body>

  <section class="card card-back">
    <div class="texture" role="img" aria-label="Soft blue diagonal architectural stripe pattern"></div>
    <div class="brand-name"><span class="brand-square"></span>Belford &amp; Company</div>
  </section>

  <section class="card card-front">
    <div class="brand-name"><span class="brand-square"></span><span>Belford &amp;<br>Company</span></div>
    <div class="divider"></div>
    <div class="contact">
      <h1 class="person-name">DANIEL HART</h1>
      <p class="person-title">Your Title</p>
      <ul class="contact-list">
        <li>
          <svg viewBox="0 0 10 10"><path d="M5 0a3.5 3.5 0 0 0-3.5 3.5C1.5 6 5 10 5 10s3.5-4 3.5-6.5A3.5 3.5 0 0 0 5 0zm0 5a1.4 1.4 0 1 1 0-2.8A1.4 1.4 0 0 1 5 5z"/></svg>
          <span>2480 Harbor Blvd., Suite #310<br>Seaport, FL 32000</span>
        </li>
        <li class="gap">
          <svg viewBox="0 0 10 10"><circle cx="5" cy="5" r="5"/><path d="M3.2 2.6l1 1-.5.7c.4.8 1 1.4 1.8 1.8l.7-.5 1 1-.6.8C4.8 7.3 2.7 5.2 2.4 3.2z" fill="#fff"/></svg>
          <span>555 210 7821</span>
        </li>
        <li>
          <svg viewBox="0 0 10 10"><circle cx="5" cy="5" r="5"/><rect x="3.5" y="2.2" width="3" height="5.6" rx="0.6" fill="#fff"/></svg>
          <span>555 318 6093</span>
        </li>
        <li>
          <svg viewBox="0 0 10 10"><rect x="0" y="3" width="3" height="7"/><rect x="3.5" y="0" width="6.5" height="10"/><rect x="5" y="1.5" width="3.5" height="2" fill="#fff"/></svg>
          <span>555 427 3158</span>
        </li>
        <li class="gap">
          <svg viewBox="0 0 10 10"><rect x="0" y="1.5" width="10" height="7"/><path d="M0 1.5l5 4 5-4" fill="none" stroke="#fff" stroke-width="1"/></svg>
          <span>info@belfordandcompany.example</span>
        </li>
        <li>
          <svg viewBox="0 0 10 10"><circle cx="5" cy="5" r="5"/><path d="M0 5h10M5 0c-2.5 3-2.5 7 0 10M5 0c2.5 3 2.5 7 0 10" fill="none" stroke="#fff" stroke-width="0.7"/></svg>
          <span>www.belfordandcompany.example</span>
        </li>
      </ul>
    </div>
    <div class="slogan-band">Precision Defines Every Deal</div>
  </section>

</body>
</html>
```